Renata Quisby

Luxury And Style -

Black - White & Gold

Target Market(s)

Fashion

Industry/Entity Type

Fashion

Requirements
Must have
• High-End
Nice to have
• We will Print on Silk Paper

```html
<!DOCTYPE html>
<html lang="en">
<head>
<meta charset="utf-8">
<title>Renata Quisby Letterhead</title>
<link rel="stylesheet" href="https://fonts.googleapis.com/css2?family=Arimo:wght@400;700&family=Montserrat:wght@400&display=swap">
<style>
  :root {
    --backdrop: #e9e9ea;
    --paper: #f3f3f3;
    --ink: #1a1a1a;
    --gold: #b98d5c;
    --gold-light: #d6b48a;
    --navy: #0e0f26;
    --placeholder: #dcdcdc;
  }
  * { margin: 0; padding: 0; box-sizing: border-box; }
  html, body { width: 1200px; height: 795px; overflow: hidden; }
  body {
    background: var(--backdrop);
    font-family: "Arimo", Arial, sans-serif;
    color: var(--ink);
    position: relative;
  }
  .letterhead {
    position: absolute;
    left: 330px;
    top: 15px;
    width: 540px;
    height: 764px;
    background: var(--paper);
    box-shadow: 0 6px 22px rgba(0,0,0,0.12);
    overflow: hidden;
  }
  .brand {
    position: absolute;
    left: 44px;
    top: 62px;
    display: flex;
    align-items: center;
    gap: 8px;
  }
  .brand-mark {
    width: 12px;
    height: 12px;
    border-radius: 50%;
    background: var(--gold);
    flex: none;
  }
  .brand-name {
    font-family: "Arimo", Arial, sans-serif;
    font-weight: 700;
    font-size: 16px;
    color: var(--gold);
  }
  .contact {
    position: absolute;
    left: 352px;
    top: 44px;
    padding-left: 12px;
    border-left: 1px solid var(--gold);
    font-size: 7.5px;
    line-height: 1.55;
  }
  .contact-row { display: flex; align-items: center; gap: 4px; }
  .contact-icon { width: 7px; height: 7px; flex: none; }
  .recipient {
    position: absolute;
    left: 44px;
    top: 142px;
    font-size: 9px;
    line-height: 1.3;
  }
  .recipient-name { font-weight: 700; font-size: 10px; }
  .letter-body {
    position: absolute;
    left: 88px;
    top: 200px;
    width: 370px;
    font-size: 8.6px;
    line-height: 1.5;
  }
  .letter-body p + p { margin-top: 14px; }
  .sign-off {
    position: absolute;
    left: 88px;
    top: 418px;
    font-size: 9px;
  }
  .signature {
    width: 150px;
    height: 60px;
    margin: 4px 0 4px 18px;
    background: var(--placeholder);
    border-radius: 4px;
  }
  .signer-name { font-weight: 700; font-size: 10px; margin-left: 50px; }
  .signer-title { font-size: 9.5px; margin-left: 50px; }
  .footer-wave { position: absolute; left: 0; bottom: 0; width: 540px; height: 230px; }
  .footer-web {
    position: absolute;
    right: 34px;
    bottom: 34px;
    color: #ffffff;
    font-family: "Montserrat", Arial, sans-serif;
    font-size: 7.5px;
    letter-spacing: 2px;
    text-transform: uppercase;
  }
</style>
</head>
<body>
  <main class="letterhead">
    <header>
      <div class="brand">
        <span class="brand-mark"></span>
        <span class="brand-name">Renata Quisby</span>
      </div>
      <div class="contact">
        <div class="contact-row">
          <svg class="contact-icon" viewBox="0 0 10 10"><circle cx="5" cy="5" r="5" fill="var(--gold)"/><path d="M3 2.5l1.3 0 .5 1.4-.8.6a4 4 0 0 0 1.5 1.5l.6-.8 1.4.5v1.3c-3 .3-5-2-4.5-4.5z" fill="#fff"/></svg>
          <span>(555) 214-0388</span>
        </div>
        <div class="contact-row">
          <svg class="contact-icon" viewBox="0 0 10 10"><circle cx="5" cy="5" r="5" fill="var(--gold)"/><path d="M3 2.5l1.3 0 .5 1.4-.8.6a4 4 0 0 0 1.5 1.5l.6-.8 1.4.5v1.3c-3 .3-5-2-4.5-4.5z" fill="#fff"/></svg>
          <span>(555) 214-0390</span>
        </div>
        <div class="contact-row">
          <svg class="contact-icon" viewBox="0 0 10 10"><circle cx="5" cy="5" r="5" fill="var(--gold)"/><rect x="2.5" y="3.3" width="5" height="3.5" fill="none" stroke="#fff" stroke-width="0.7"/><path d="M2.5 3.3L5 5.3 7.5 3.3" fill="none" stroke="#fff" stroke-width="0.7"/></svg>
          <span>hello@quisbystudio.com</span>
        </div>
      </div>
    </header>

    <section class="recipient">
      <div class="recipient-name">TOMAS VERHOE</div>
      <div>Street Name,City Name.</div>
      <div>Zip Coad 0000</div>
    </section>

    <article class="letter-body">
      <p>Lorem Ipsum is simply dummy text of the printing and typesetting industry. Lorem Ipsum has been the industry's standard dummy text ever since the 1500s, when an unknown printer took a galley of type and scrambled it to make a type specimen book. It has survived not only five centuries,but also the leap into electronic typesetting, remaining essentially unchanged. It was popularised in the 1960s with the release of Typeleaf sheets containing Lorem Ipsum passages, and more recently with desktop publishing software like Pagecraft Studio including versions of Lorem Ipsum.</p>
      <p>It is a long established fact that a reader will be distracted by the readable content of a page when looking at its layout. The point of using Lorem Ipsum is that it has a more-or-less normal distribution of letters, as opposed to using 'Content here, content here', making it look like readable English. Many desktop and at i years, sometimes by accident, sometimes on purpose (injected humour and the like).</p>
    </article>

    <section class="sign-off">
      <div>Regards,</div>
      <div class="signature" role="img" aria-label="Handwritten signature of Tomas D Verhoe"></div>
      <div class="signer-name">Tomas D Verhoe</div>
      <div class="signer-title">General Maneger</div>
    </section>

    <footer>
      <svg class="footer-wave" viewBox="0 0 540 230" preserveAspectRatio="none">
        <defs>
          <linearGradient id="goldBand" x1="0" y1="0" x2="1" y2="0">
            <stop offset="0" stop-color="var(--gold-light)"/>
            <stop offset="0.6" stop-color="var(--gold)"/>
            <stop offset="1" stop-color="var(--gold-light)"/>
          </linearGradient>
        </defs>
        <path d="M0 150 C180 150 360 110 540 0 L540 230 L0 230 Z" fill="url(#goldBand)"/>
        <path d="M0 162 C200 160 380 120 540 14 L540 230 L0 230 Z" fill="var(--navy)"/>
      </svg>
      <div class="footer-web">www.quisbystudio.com</div>
    </footer>
  </main>
</body>
</html>
```